plumbing & gas fitting business card design

We need a business card design for a plumbing & gas fitting company. The company covers commercial, domestic and maintenance work. We would like a modern design communicating efficiency and sophistication. preferred colours would include (red grey & black) or (green grey & black). Please DO NOT include any water droplets.

Industry/Entity Type

Business

Contact Information for Business Card

Vortig Plumbing & Gas, Commercial Domestic & Maintenance, licence no. 617394K, ABN 47215830962, Phone 0417382956, Email vortigplumbingandgas@corvanet.com

```html
<!DOCTYPE html>
<html lang="en">
<head>
<meta charset="utf-8">
<title>Vortig Plumbing &amp; Gas – Business Card</title>
<link href="https://fonts.googleapis.com/css2?family=Arimo:wght@400;700&display=swap" rel="stylesheet">
<style>
  :root {
    --page-bg: #ecebea;
    --card-red: #8e3626;
    --card-red-dark: #5e1f15;
    --card-red-light: #a84a36;
    --band-grey: #c9c7c4;
    --band-grey-dark: #8f8c88;
    --ink: #0d0d0d;
    --logo-box: #c9c2b8;
    --logo-black: #111111;
    --logo-text: #ffffff;
    --photo-skin: #b9836a;
    --photo-leather: #6a2e1d;
  }
  * { box-sizing: border-box; margin: 0; padding: 0; }
  html, body {
    width: 1200px; height: 686px; overflow: hidden;
    background: var(--page-bg);
    font-family: "Arimo", Arial, sans-serif;
  }
  .card {
    position: absolute; left: 150px; top: 68px;
    width: 900px; height: 550px;
    background: linear-gradient(160deg, var(--card-red-light), var(--card-red) 45%, var(--card-red-dark));
    overflow: hidden;
    box-shadow: 0 10px 30px rgba(0,0,0,.25);
  }
  .top-strip {
    position: absolute; left: 0; top: 0; width: 100%; height: 28px;
    background: linear-gradient(90deg, #d9d6d2, #b9b5b0);
  }
  .contact-band {
    position: absolute; left: 0; top: 28px; width: 100%; height: 150px;
    background: linear-gradient(180deg, var(--card-red-light), var(--card-red));
  }
  .detail-band {
    position: absolute; left: 0; top: 178px; width: 100%; height: 110px;
    background: linear-gradient(90deg, var(--band-grey-dark), var(--band-grey) 40%, #dedbd7);
  }
  .tool-photo {
    position: absolute; right: 0; top: 0; width: 360px; height: 100%;
    background: linear-gradient(200deg, #d8d4cf 0%, var(--photo-skin) 35%, var(--photo-leather) 75%, #3d1a10 100%);
  }
  .phone, .email {
    position: absolute; left: 36px; display: flex; align-items: center; color: var(--ink); font-weight: 700;
  }
  .phone { top: 48px; font-size: 48px; gap: 16px; }
  .email { top: 122px; font-size: 23px; font-weight: 400; gap: 14px; }
  .phone svg { width: 34px; height: 34px; }
  .email svg { width: 24px; height: 24px; }
  .registration {
    position: absolute; top: 214px; left: 36px; display: flex; gap: 60px;
    font-size: 28px; color: var(--ink);
  }
  .logo {
    position: absolute; left: 36px; top: 322px; width: 420px; height: 112px;
    background: var(--logo-box); border: 3px solid var(--logo-black);
    display: flex; align-items: center; justify-content: center;
  }
  .logo-name {
    font-weight: 700; font-size: 33px; color: var(--logo-black); letter-spacing: 1px;
  }
  .services {
    position: absolute; left: 36px; top: 448px; font-size: 24px; font-weight: 700; color: var(--ink);
  }
</style>
</head>
<body>
  <div class="card">
    <div class="top-strip"></div>
    <div class="contact-band"></div>
    <div class="detail-band"></div>
    <div class="tool-photo" role="img" aria-label="Photo of a plumber's hands reaching into a leather tool belt holding a pipe wrench and screwdrivers"></div>

    <div class="phone">
      <svg viewBox="0 0 24 24" aria-hidden="true"><path fill="#0d0d0d" d="M6.6 10.8a15.1 15.1 0 0 0 6.6 6.6l2.2-2.2c.3-.3.7-.4 1-.2 1.1.4 2.3.6 3.6.6.6 0 1 .4 1 1V20c0 .6-.4 1-1 1A17 17 0 0 1 3 4c0-.6.4-1 1-1h3.5c.6 0 1 .4 1 1 0 1.3.2 2.5.6 3.6.1.3 0 .7-.2 1z"/></svg>
      <span>0417382956</span>
    </div>
    <div class="email">
      <svg viewBox="0 0 24 24" aria-hidden="true"><rect x="2" y="5" width="17" height="15" fill="none" stroke="#0d0d0d" stroke-width="2"/><path d="M9 15l1-4 10-9 3 3-10 9z" fill="#0d0d0d"/></svg>
      <span>vortigplumbingandgas@corvanet.com</span>
    </div>

    <div class="registration">
      <span class="licence">licence 617394K</span>
      <span class="abn">abn 47215830962</span>
    </div>

    <div class="logo">
      <span class="logo-name">VORTIG PLUMBING &amp; GAS</span>
    </div>
    <div class="services">Commercial Domestic &amp; Maintenance</div>
  </div>
</body>
</html>
```